Book Cover and Logo Design

We want a cover designed for a book titled, "The Open Harvest Blueprint" Subtitled "The Decade Program to Rebuild Society, Dissolve the Levy Maze, Clear the Public Ledger, and Revive the Shared Promise" and a logo that we can use on social media when talking about The Open Harvest Blueprint.

This book succeeds Mending Horizon, on the website https://www.mendinghorizon.example

You can see The Open Harvest Blueprint on the website. It gives American's basic income, free healthcare, and free college while slashing personal income taxes and paying off the national debt. The Tide Levy that would replace income taxes would also fund huge infrastructure projects like high speed mag lev trains criss-crossing the nation, a moon base, major desalinization projects to provide water for Western cities and farms.

Target Market(s)

American voters

Industry/Entity Type

American economic policy

Requirements
Must have
• the book cover should be exciting, portraying images of a futuristic America, but with nature tucked into the scenes too
Nice to have
• Patriotic colors
Should not have
• Nothing partisan at all

```html
<!DOCTYPE html>
<html lang="en">
<head>
<meta charset="utf-8">
<title>Open Harvest Blueprint — Book Cover</title>
<link rel="stylesheet" href="https://fonts.googleapis.com/css2?family=Passion+One:wght@700&family=Literata:wght@400&display=swap">
<style>
  :root {
    --cover-blue: #2b3592;
    --spine-line: #232b7c;
    --title-white: #f3f2ef;
    --text-white: #eeeef4;
    --art-sky: #d6e5f4;
    --art-mid: #8fb0cf;
    --art-land: #7f9c6a;
    --art-base: #3a4aa0;
  }
  * { margin: 0; padding: 0; box-sizing: border-box; }
  html, body { width: 887px; height: 1200px; overflow: hidden; background: var(--cover-blue); }
  .cover {
    position: relative;
    width: 887px;
    height: 1200px;
    background: var(--cover-blue);
    overflow: hidden;
  }
  .spine-fold {
    position: absolute;
    left: 40px; top: 0;
    width: 2px; height: 100%;
    background: var(--spine-line);
  }
  .author {
    position: absolute;
    top: 66px; left: 0; width: 100%;
    text-align: center;
    font-family: "Literata", Georgia, serif;
    font-size: 27px;
    color: var(--text-white);
    letter-spacing: 0.5px;
  }
  .title {
    position: absolute;
    top: 140px; left: 98px;
    font-family: "Passion One", "Arial Black", sans-serif;
    font-weight: 700;
    font-size: 184px;
    line-height: 176px;
    color: var(--title-white);
    letter-spacing: -1px;
    z-index: 2;
  }
  .title span { display: block; }
  .subtitle {
    position: absolute;
    top: 722px; left: 102px;
    font-family: "Literata", Georgia, serif;
    font-size: 23px;
    line-height: 27px;
    color: var(--text-white);
  }
  .subtitle span { display: block; }
  .cover-art {
    position: absolute;
    left: 466px; top: 552px;
    width: 316px; height: 648px;
    border-radius: 158px 158px 0 0;
    background: linear-gradient(180deg, var(--art-sky) 0%, var(--art-mid) 40%, var(--art-land) 70%, var(--art-base) 100%);
  }
  .imprint {
    position: absolute;
    left: 101px; top: 1072px;
    font-family: "Passion One", "Arial Black", sans-serif;
    font-weight: 700;
    font-size: 24px;
    line-height: 22px;
    color: var(--title-white);
  }
  .imprint span { display: block; }
</style>
</head>
<body>
<main class="cover">
  <div class="spine-fold"></div>

  <div class="cover-art" role="img" aria-label="Illustration: a couple seen from behind walking along a path of light toward a keyhole-shaped opening that reveals a sunlit sky over green hills and a river"></div>

  <p class="author">Daniel Reed Whitaker</p>

  <h1 class="title">
    <span>Open</span>
    <span>Harvest</span>
    <span>Blueprint</span>
  </h1>

  <p class="subtitle">
    <span>The Decade Program</span>
    <span>to Rebuild Society,</span>
    <span>Dissolve the Levy Maze,</span>
    <span>Clear the Public Ledger,</span>
    <span>and Revive</span>
    <span>the Shared Promise</span>
  </p>

  <div class="imprint">
    <span>Open</span>
    <span>Harvest</span>
    <span>Blueprint</span>
  </div>
</main>
</body>
</html>
```